I need a book cover design for my book "Roaming Quartets." It is a non-fiction book focused on answering the question of whether American evangelicals look more like the Quartets than Jesus.

The subtitle is "The Curious Habits of Norway's Traveling Fiddlers and Their Seaside Rivals." The author name is Dorian Whitlock.

I will be publishing this as an ebook and paperback.

I am open to all ideas, but will share the only thought I had as a possible design. In the title, the third letter in both words is "A." I thought about the idea of having the "A" in "Roaming" have a halo and the "A" in "Quartets" somehow seem to be a shadow of that first "A" but have devil horns instead of a halo. Again, I'm not sold on that, but am sharing it as one design possibility.

I am not interested in the book cover design having a cheesy religious look to it (as many do). I am more interested in it looking like a professional non-fiction cover.

```html
<!DOCTYPE html>
<html lang="en">
<head>
<meta charset="utf-8">
<title>Roaming Quartets — Dorian Whitlock</title>
<link rel="stylesheet" href="https://fonts.googleapis.com/css2?family=Anton&family=Archivo+Black&display=swap">
<style>
  :root {
    --sky-top: #e8170f;
    --sky-low: #f2461a;
    --sun-core: #fff03a;
    --sun-edge: #ffc21e;
    --water-top: #ffe44a;
    --water-mid: #f5861a;
    --water-deep: #d8180f;
    --ink: #0b0b0b;
    --rule: #fff7a8;
    --halo-tone: #f6c21c;
    --horn-tone: #d4140c;
  }
  html, body {
    margin: 0;
    padding: 0;
    width: 756px;
    height: 1200px;
    overflow: hidden;
    background: #ffffff;
  }
  .cover {
    position: relative;
    width: 756px;
    height: 1200px;
    overflow: hidden;
    font-family: "Archivo Black", "Arial Black", sans-serif;
    color: var(--ink);
  }
  .cover__scene {
    position: absolute;
    inset: 0;
    background: linear-gradient(to bottom,
      var(--sky-top) 0, var(--sky-low) 508px,
      var(--water-top) 510px, var(--water-top) 590px,
      var(--water-mid) 760px, var(--water-deep) 1200px);
  }
  .cover__sun {
    position: absolute;
    left: 0;
    top: 0;
    width: 756px;
    height: 510px;
    background: radial-gradient(circle at 395px 430px,
      var(--sun-core) 0, var(--sun-core) 230px, var(--sun-edge) 280px, rgba(255,170,30,0) 288px);
  }
  .title {
    position: absolute;
    left: 0;
    top: 0;
    width: 756px;
    height: 480px;
  }
  .title__word {
    font-family: "Anton", "Impact", sans-serif;
    fill: var(--ink);
  }
  .title__halo-area { fill: var(--halo-tone); }
  .title__horn-area { fill: var(--horn-tone); opacity: 0.85; }
  .subtitle-block {
    position: absolute;
    left: 105px;
    top: 604px;
    width: 548px;
  }
  .subtitle-block__rule {
    height: 5px;
    background: var(--rule);
  }
  .subtitle {
    margin: 24px 0 30px;
    font-size: 25px;
    line-height: 34px;
    text-align: center;
  }
  .author {
    position: absolute;
    left: 0;
    width: 756px;
    top: 1068px;
    margin: 0;
    font-size: 62px;
    line-height: 70px;
    text-align: center;
    letter-spacing: 1px;
  }
</style>
</head>
<body>
  <main class="cover">
    <div class="cover__scene" role="img" aria-label="Sunset photograph: a large yellow sun setting over rippling orange and red sea under a red sky">
      <div class="cover__sun"></div>
    </div>

    <svg class="title" viewBox="0 0 756 480" aria-labelledby="book-title">
      <title id="book-title">Roaming Quartets</title>
      <text class="title__word" x="24" y="264" font-size="136" textLength="709" lengthAdjust="spacingAndGlyphs">ROAMING</text>
      <text class="title__word" x="24" y="450" font-size="195" textLength="709" lengthAdjust="spacingAndGlyphs">QUARTETS</text>
      <rect class="title__halo-area" x="240" y="130" width="50" height="10" rx="5" role="img" aria-label="Illustration: golden halo above the letter A"/>
      <rect class="title__horn-area" x="200" y="270" width="110" height="170" rx="8" role="img" aria-label="Illustration: pair of red devil horns over the letter A"/>
    </svg>

    <section class="subtitle-block">
      <div class="subtitle-block__rule"></div>
      <p class="subtitle">The Curious Habits of Norway's Traveling Fiddlers and Their Seaside Rivals.</p>
      <div class="subtitle-block__rule"></div>
    </section>

    <p class="author">DORIAN WHITLOCK</p>
  </main>
</body>
</html>
```